Tarvell homes and renovations business card design.

Would like some new card designs utilizing my new logo that look professional. I am open to different colors on the logo or utilize the same ones we have. I like the original concept but would like to see some fresh ideas and build on what we have already done.

Target Market(s)

Custom home building industry, Real estate sales, Renovation projects.

Industry/Entity Type

Home Builder

Contact Information for Business Card

Tarvell Homes and Renovations
2871 162nd Street
Wrenford, Northvale
T0L3P0
Home : 780- 555-0187 Cell: 780- 555-0243

My info is : Gus Tarvell, President and CEO
email: tarvellhomes@quillmail.example
Website: tarvellhomes.example

Requirements
Must have
• Must Use my new logo design. I am open to different colors on the logo or utilize the same ones in the existing design. I can upload the original logo design if needed.

```html
<!DOCTYPE html>
<html lang="en">
<head>
<meta charset="utf-8">
<title>Tarvell Homes and Renovations – Business Cards</title>
<link href="https://fonts.googleapis.com/css2?family=Montserrat:wght@400;500;600&display=swap" rel="stylesheet">
<style>
  :root {
    --gold: #a8800f;
    --gold-deep: #8f6a06;
    --yellow: #f5c400;
    --grey-text: #555559;
    --card: #ffffff;
    --backdrop: #e9e6e2;
  }
  * { margin: 0; padding: 0; box-sizing: border-box; }
  html, body { width: 1200px; height: 800px; overflow: hidden; }
  body {
    background: var(--backdrop);
    font-family: "Montserrat", sans-serif;
    display: flex;
    align-items: center;
    justify-content: center;
    gap: 60px;
  }
  .card {
    position: relative;
    width: 525px;
    height: 300px;
    background: var(--card);
    box-shadow: 0 10px 30px rgba(0,0,0,0.15);
    overflow: hidden;
  }

  /* Front: brand name */
  .card-front {
    display: flex;
    align-items: center;
    justify-content: center;
  }
  .brand {
    display: flex;
    align-items: center;
    gap: 18px;
  }
  .brand-mark {
    width: 22px;
    height: 22px;
    background: var(--gold);
  }
  .brand-name {
    color: var(--gold);
    font-weight: 600;
    line-height: 1.05;
    text-transform: uppercase;
  }
  .card-front .brand-name { font-size: 54px; }
  .card-front .brand-name span { display: block; font-size: 19.5px; letter-spacing: 0.06em; }

  /* Back: contact details */
  .card-back .brand {
    position: absolute;
    left: 92px;
    top: 34px;
    gap: 10px;
  }
  .card-back .brand-mark { width: 10px; height: 10px; }
  .card-back .brand-name { font-size: 26px; }
  .card-back .brand-name span { display: block; font-size: 9.4px; letter-spacing: 0.06em; }

  .person {
    position: absolute;
    left: 60px;
    top: 112px;
  }
  .person-name {
    color: var(--gold);
    font-weight: 600;
    font-size: 20px;
    text-transform: uppercase;
  }
  .person-title {
    color: var(--grey-text);
    font-size: 13px;
    font-weight: 500;
    margin-top: 2px;
  }

  .wave {
    position: absolute;
    left: 0;
    bottom: 0;
    width: 525px;
    height: 300px;
  }

  .contacts {
    position: absolute;
    right: 24px;
    top: 118px;
    list-style: none;
    display: flex;
    flex-direction: column;
    gap: 8px;
  }
  .contact {
    display: flex;
    align-items: center;
    justify-content: flex-end;
    gap: 10px;
    color: var(--grey-text);
    font-size: 12.5px;
    font-weight: 500;
    text-align: right;
    line-height: 1.3;
  }
  .contact-icon {
    flex: none;
    width: 26px;
    height: 26px;
    border-radius: 50%;
    background: var(--gold);
    display: flex;
    align-items: center;
    justify-content: center;
  }
  .contact-icon svg { width: 14px; height: 14px; }
</style>
</head>
<body>

  <section class="card card-front">
    <div class="brand">
      <div class="brand-mark"></div>
      <div class="brand-name">Tarvell<span>Homes and Renovations</span></div>
    </div>
  </section>

  <section class="card card-back">
    <div class="brand">
      <div class="brand-mark"></div>
      <div class="brand-name">Tarvell<span>Homes and Renovations</span></div>
    </div>

    <div class="person">
      <div class="person-name">Gus Tarvell</div>
      <div class="person-title">President and CEO</div>
    </div>

    <svg class="wave" viewBox="0 0 525 300" preserveAspectRatio="none">
      <defs>
        <linearGradient id="bandGold" x1="0" y1="0" x2="1" y2="0">
          <stop offset="0" stop-color="#9c7608"/>
          <stop offset="0.6" stop-color="#c49a10"/>
          <stop offset="1" stop-color="#b48a0c"/>
        </linearGradient>
        <linearGradient id="bandYellow" x1="0" y1="0" x2="1" y2="0">
          <stop offset="0" stop-color="#d9a800"/>
          <stop offset="0.5" stop-color="#ffcc00"/>
          <stop offset="1" stop-color="#f2bd00"/>
        </linearGradient>
      </defs>
      <path d="M0 168 C 90 150, 170 170, 240 230 C 300 282, 360 300, 430 300 L 0 300 Z" fill="url(#bandGold)"/>
      <path d="M0 215 C 90 175, 180 195, 250 245 C 310 290, 380 285, 525 262 L 525 300 L 0 300 Z" fill="url(#bandYellow)"/>
      <path d="M0 262 C 100 230, 190 250, 260 280 C 300 296, 340 300, 380 300 L 0 300 Z" fill="var(--gold-deep)" opacity="0.85"/>
    </svg>

    <ul class="contacts">
      <li class="contact">
        <span>780- 555-0187<br>780- 555-0243</span>
        <span class="contact-icon"><svg viewBox="0 0 24 24"><path fill="#fff" d="M6.6 10.8a15 15 0 0 0 6.6 6.6l2.2-2.2a1 1 0 0 1 1-.25 11.4 11.4 0 0 0 3.6.57 1 1 0 0 1 1 1V20a1 1 0 0 1-1 1A17 17 0 0 1 3 4a1 1 0 0 1 1-1h3.5a1 1 0 0 1 1 1c0 1.25.2 2.45.57 3.57a1 1 0 0 1-.25 1z"/></svg></span>
      </li>
      <li class="contact">
        <span>tarvellhomes@quillmail.example</span>
        <span class="contact-icon"><svg viewBox="0 0 24 24"><rect x="3" y="6" width="18" height="12" rx="1" fill="#fff"/><path d="M3 6l9 7 9-7" fill="none" stroke="#a8800f" stroke-width="1.6"/></svg></span>
      </li>
      <li class="contact">
        <span>tarvellhomes.example</span>
        <span class="contact-icon"><svg viewBox="0 0 24 24"><circle cx="12" cy="12" r="8" fill="none" stroke="#fff" stroke-width="2"/><path d="M4 12h16M12 4c3 3 3 13 0 16M12 4c-3 3-3 13 0 16" fill="none" stroke="#fff" stroke-width="1.5"/></svg></span>
      </li>
      <li class="contact">
        <span>2871 162nd Street<br>Wrenford, Northvale T0L3P0</span>
        <span class="contact-icon"><svg viewBox="0 0 24 24"><path fill="#fff" d="M12 3l9 8h-3v9h-4v-6h-4v6H6v-9H3z"/></svg></span>
      </li>
    </ul>
  </section>

</body>
</html>
```